One-Page Flat Design for SEO Company [2 DAYS]

We need a one-page flat design for our SEO company. Our current website is http://www.rankorchard.com/. We are looking to completely re-design the site using new flat design techniques.
Below are some examples of the type of style we're going after:
http://pelmora.com/
http://tobyharlan.co.uk/
https://quillet.co/
http://marcusfenley.me/
As you can see- flat, clean, minimal. It is very important you follow this type of style.
For colour scheme, you may use one of the pre-made colour palettes from here:
http://www.wavecrestlab.com/blog/inspiration/24-flat-designs-with-compelling-color-palettes
I've attached a wireframe to be followed.
Hi,

```html
<!DOCTYPE html>
<html lang="en">
<head>
<meta charset="utf-8">
<title>RankOrchard — SEO Services</title>
<link rel="stylesheet" href="https://fonts.googleapis.com/css2?family=Oswald:wght@500;600&family=Open+Sans:wght@400;600&family=Arimo:wght@400&family=Noto+Serif:ital@1&display=swap">
<style>
:root{
  --orange:#f57c00;
  --orange-light:#ffa200;
  --orange-deep:#ff7a00;
  --black:#000;
  --hero:#121212;
  --white:#fff;
  --grey-line:#dcdcdc;
  --grey-text:#8a8a8a;
  --ink:#333;
  --green:#4cae4c;
  --red:#e7624c;
  --blue:#5b8fc9;
}
*{margin:0;padding:0;box-sizing:border-box}
html,body{width:1200px;height:2894px;overflow:hidden}
body{position:relative;background:var(--white);font-family:"Open Sans",sans-serif;color:var(--ink)}
section,header,footer{position:absolute;left:0;width:1200px}

/* brand lockup: plain name in the text font with one circle */
.brand{position:absolute;display:flex;align-items:center;gap:12px}
.brand-dot{width:24px;height:24px;border-radius:50%;background:var(--orange)}
.brand-name{font-family:"Open Sans",sans-serif;font-weight:600;font-size:34px;color:var(--white);line-height:1}

/* header */
.site-header{top:0;height:135px;background:var(--black)}
.site-header .brand{left:72px;top:46px}
.nav{position:absolute;top:0;left:689px;display:flex;height:132px}
.nav a{font-family:"Oswald",sans-serif;font-weight:500;font-size:16px;color:var(--white);text-decoration:none;display:flex;align-items:center;padding:0 13px;height:100%}
.nav a.active{background:linear-gradient(var(--orange-light),var(--orange-deep));color:var(--black);width:51px;padding:0;justify-content:center}

/* hero */
.hero{top:135px;height:486px;background:var(--hero)}
.hero h1{position:absolute;left:73px;top:100px;font-family:"Oswald",sans-serif;font-weight:600;font-size:45px;line-height:80px;color:var(--white);letter-spacing:.5px}
.hero p{position:absolute;left:73px;top:265px;width:620px;font-family:"Arimo",sans-serif;font-size:19px;line-height:35px;color:#ccc}
.dots{position:absolute;left:73px;top:390px;display:flex;gap:9px}
.dots span{width:13px;height:13px;border-radius:50%;background:var(--white)}
.dots span:first-child{background:var(--orange)}
.hero-art{position:absolute;left:743px;top:58px;width:370px;height:370px;border-radius:16px;background:radial-gradient(circle at 55% 45%,#b7e0ff 0,#e8c84a 30%,#c73a3a 60%,var(--hero) 75%)}

/* titles */
.section-title{position:absolute;left:0;width:1200px;text-align:center;font-family:"Oswald",sans-serif;font-weight:600;font-size:33px;color:var(--orange)}
.section-sub{position:absolute;left:0;width:1200px;text-align:center;font-size:15px;color:var(--black)}

/* feature circles */
.feature{position:absolute;width:200px;text-align:center}
.feature .ring{width:128px;height:128px;margin:0 auto;border-radius:50%;border:3px solid #b5b5b5;display:flex;align-items:center;justify-content:center;background:var(--white)}
.feature.on .ring{background:var(--orange);border-color:var(--orange)}
.feature .label{margin-top:30px;font-size:16px;color:var(--grey-text)}
.feature.on .label{color:var(--orange)}

.why{top:621px;height:411px}
.packages{top:1032px;height:550px;background:linear-gradient(#f3f3f3,#fff 40%,#eee)}

/* pricing */
.pricing{position:absolute;left:83px;top:103px;width:1042px;height:403px;background:var(--white);border:2px solid var(--grey-line);border-radius:4px}
.plan{position:absolute;top:0;width:260px;height:100%;text-align:center}
.plan + .plan{border-left:1px solid #eee}
.plan.featured{top:-14px;height:433px;border:3px solid #f5a623;border-radius:4px;background:linear-gradient(#fff,#fafafa);box-shadow:0 0 8px rgba(0,0,0,.15);z-index:2}
.plan h3{font-family:"Arimo",sans-serif;font-weight:400;font-size:36px;color:#333;margin-top:20px;line-height:50px}
.plan.featured h3{color:var(--orange);margin-top:32px}
.plan .price{font-family:"Noto Serif",serif;font-style:italic;font-size:20px;color:#999;line-height:30px}
.plan ul{list-style:none;width:232px;margin:22px auto 0;text-align:left}
.plan li{height:33px;border-top:1px solid #eee;display:flex;align-items:center;gap:10px;padding-left:14px;font-size:12px;color:#555}
.plan li svg{flex:none}
.signup{display:inline-flex;align-items:center;gap:10px;margin-top:28px;width:135px;height:54px;justify-content:center;border:1px solid #d5d5d5;border-radius:3px;background:linear-gradient(#fff,#eaeaea);font-weight:600;font-size:13px;color:#555}
.signup i{width:24px;height:24px;border-radius:50%;background:var(--blue);display:flex;align-items:center;justify-content:center}
.plan.featured .signup i{background:var(--orange)}
.ribbon{position:absolute;right:-3px;top:-3px;width:80px;height:80px;overflow:hidden}
.ribbon span{position:absolute;right:-28px;top:14px;width:110px;transform:rotate(45deg);background:#f5a623;color:var(--white);font-size:10px;font-weight:600;text-align:center;line-height:20px}

/* cta band */
.cta{top:1582px;height:136px;background:linear-gradient(var(--orange),#ff9d1c)}
.cta p{position:absolute;left:81px;top:53px;font-family:"Arimo",sans-serif;font-size:17px;color:var(--white)}
.cta a{position:absolute;left:826px;top:33px;width:230px;height:62px;border:2px solid var(--white);border-radius:3px;display:flex;align-items:center;justify-content:center;font-family:"Arimo",sans-serif;font-size:24px;color:var(--white);text-decoration:none}

.individual{top:1718px;height:380px}

/* contact */
.contact{top:2098px;height:507px;background:linear-gradient(#ffa600,#ff7f00)}
.contact h2{position:absolute;left:0;width:1200px;top:46px;text-align:center;font-weight:400;font-size:28px;color:var(--white)}
.contact .lead{position:absolute;left:0;width:1200px;top:110px;text-align:center;font-size:14px;color:#fff6e0}
.field{position:absolute;background:var(--white);font-size:15px;color:#c9c9c9;padding:17px 32px}
.field.textarea{padding-top:32px}

/* footer */
.site-footer{top:2605px;height:289px;background:var(--black)}
.site-footer .brand{left:482px;top:76px}
.site-footer p{position:absolute;left:0;width:1200px;top:155px;text-align:center;font-size:15px;color:var(--white)}
.social{position:absolute;left:519px;top:211px;display:flex;gap:3px}
.social span{width:38px;height:38px;border-radius:50%;background:var(--white)}
</style>
</head>
<body>

<header class="site-header">
  <div class="brand"><span class="brand-dot"></span><span class="brand-name">RankOrchard</span></div>
  <nav class="nav">
    <a class="active" href="#">HOME</a>
    <a href="#">ABOUT</a>
    <a href="#">WORK</a>
    <a href="#">SERVICES</a>
    <a href="#">TEAM</a>
    <a href="#">CONTACT US</a>
  </nav>
</header>

<section class="hero">
  <h1>FINALLY, SEO SERVICES THAT<br>ACTUALLY WORK</h1>
  <p>We provide high-quality SEO services that are guaranteed to give your rankings a boost. ...</p>
  <div class="dots"><span></span><span></span><span></span></div>
  <div class="hero-art" role="img" aria-label="Glossy 3D bar chart in red, yellow and green with a magnifying glass"></div>
</section>

<section class="why">
  <h2 class="section-title" style="top:22px">WHY CHOOSE RANKORCHARD?</h2>
  <p class="section-sub" style="top:94px">OUR COMPANY PRIDES ITSELF IN KEEPING THE PRICES LOW FOR WHATEVER IT TAKES. YOU WILL BE PLEASANTLY SURPRISED BY OUR COSTS.</p>
  <div class="feature on" style="left:232px;top:158px">
    <div class="ring"><svg width="56" height="56" viewBox="0 0 56 56" fill="none" stroke="#fff" stroke-width="5" stroke-linecap="round"><path d="M12 44 L44 12"/><path d="M12 12 L44 44"/><circle cx="12" cy="12" r="6"/><circle cx="44" cy="44" r="6"/></svg></div>
    <div class="label">BRANDING</div>
  </div>
  <div class="feature" style="left:487px;top:158px">
    <div class="ring"><svg width="56" height="50" viewBox="0 0 56 50" fill="none" stroke="#999" stroke-width="3"><rect x="4" y="4" width="48" height="32" rx="2"/><path d="M20 46h16M28 36v10"/><path d="M20 28 L38 12" stroke-linecap="round"/></svg></div>
    <div class="label">DESIGN</div>
  </div>
  <div class="feature" style="left:741px;top:158px">
    <div class="ring"><svg width="60" height="44" viewBox="0 0 60 44" fill="none" stroke="#999" stroke-width="3"><rect x="10" y="4" width="40" height="28" rx="2"/><path d="M2 38h56"/><circle cx="30" cy="18" r="5"/></svg></div>
    <div class="label">DEVELOPMENT</div>
  </div>
</section>

<section class="packages">
  <h2 class="section-title" style="top:28px;font-size:29px">RANKORCHARD PACKAGES</h2>
  <div class="pricing">
    <div class="plan" style="left:0">
      <h3>Standard</h3><p class="price">$19/month</p>
      <ul>
        <li><svg width="14" height="12"><path d="M1 6l4 4 8-9" stroke="var(--green)" stroke-width="3" fill="none"/></svg>Download-Accelerators</li>
        <li><svg width="14" height="12"><path d="M1 6l4 4 8-9" stroke="var(--green)" stroke-width="3" fill="none"/></svg>Downloads resume</li>
        <li><svg width="14" height="12"><path d="M2 1l10 10M12 1L2 11" stroke="var(--red)" stroke-width="3"/></svg>No downloads delay</li>
        <li><svg width="14" height="12"><path d="M2 1l10 10M12 1L2 11" stroke="var(--red)" stroke-width="3"/></svg>No downloads captcha</li>
        <li><svg width="14" height="12"><path d="M2 1l10 10M12 1L2 11" stroke="var(--red)" stroke-width="3"/></svg>No Advertisements</li>
      </ul>
      <div class="signup"><i><svg width="10" height="10"><path d="M3 1l4 4-4 4" stroke="#fff" stroke-width="2" fill="none"/></svg></i>SIGN UP NOW</div>
    </div>
    <div class="plan" style="left:260px">
      <h3>Premium</h3><p class="price">$39/month</p>
      <ul>
        <li><svg width="14" height="12"><path d="M1 6l4 4 8-9" stroke="var(--green)" stroke-width="3" fill="none"/></svg>Download-Accelerators</li>
        <li><svg width="14" height="12"><path d="M1 6l4 4 8-9" stroke="var(--green)" stroke-width="3" fill="none"/></svg>Downloads resume</li>
        <li><svg width="14" height="12"><path d="M1 6l4 4 8-9" stroke="var(--green)" stroke-width="3" fill="none"/></svg>No downloads delay</li>
        <li><svg width="14" height="12"><path d="M2 1l10 10M12 1L2 11" stroke="var(--red)" stroke-width="3"/></svg>No downloads captcha</li>
        <li><svg width="14" height="12"><path d="M2 1l10 10M12 1L2 11" stroke="var(--red)" stroke-width="3"/></svg>No Advertisements</li>
      </ul>
      <div class="signup"><i><svg width="10" height="10"><path d="M3 1l4 4-4 4" stroke="#fff" stroke-width="2" fill="none"/></svg></i>SIGN UP NOW</div>
    </div>
    <div class="plan featured" style="left:504px;width:284px">
      <div class="ribbon"><span>POPULAR</span></div>
      <h3>Professional</h3><p class="price">$59/month</p>
      <ul>
        <li><svg width="14" height="12"><path d="M1 6l4 4 8-9" stroke="var(--green)" stroke-width="3" fill="none"/></svg>Download-Accelerators</li>
        <li><svg width="14" height="12"><path d="M1 6l4 4 8-9" stroke="var(--green)" stroke-width="3" fill="none"/></svg>Downloads resume</li>
        <li><svg width="14" height="12"><path d="M1 6l4 4 8-9" stroke="var(--green)" stroke-width="3" fill="none"/></svg>No downloads delay</li>
        <li><svg width="14" height="12"><path d="M1 6l4 4 8-9" stroke="var(--green)" stroke-width="3" fill="none"/></svg>No downloads captcha</li>
        <li><svg width="14" height="12"><path d="M2 1l10 10M12 1L2 11" stroke="var(--red)" stroke-width="3"/></svg>No Advertisements</li>
      </ul>
      <div class="signup"><i><svg width="10" height="10"><path d="M3 1l4 4-4 4" stroke="#fff" stroke-width="2" fill="none"/></svg></i>SIGN UP NOW</div>
    </div>
    <div class="plan" style="left:780px">
      <h3>Plus</h3><p class="price">$99/month</p>
      <ul>
        <li><svg width="14" height="12"><path d="M1 6l4 4 8-9" stroke="var(--green)" stroke-width="3" fill="none"/></svg>Download-Accelerators</li>
        <li><svg width="14" height="12"><path d="M1 6l4 4 8-9" stroke="var(--green)" stroke-width="3" fill="none"/></svg>Downloads resume</li>
        <li><svg width="14" height="12"><path d="M1 6l4 4 8-9" stroke="var(--green)" stroke-width="3" fill="none"/></svg>No downloads delay</li>
        <li><svg width="14" height="12"><path d="M1 6l4 4 8-9" stroke="var(--green)" stroke-width="3" fill="none"/></svg>No downloads captcha</li>
        <li><svg width="14" height="12"><path d="M1 6l4 4 8-9" stroke="var(--green)" stroke-width="3" fill="none"/></svg>No Advertisements</li>
      </ul>
      <div class="signup"><i><svg width="10" height="10"><path d="M3 1l4 4-4 4" stroke="#fff" stroke-width="2" fill="none"/></svg></i>SIGN UP NOW</div>
    </div>
  </div>
</section>

<section class="cta">
  <p>The lorem ipsum text is typically a mangled section of De finibus bonorum et malorum</p>
  <a href="#">Request Quote</a>
</section>

<section class="individual">
  <h2 class="section-title" style="top:26px">INDIVIDUAL SEO SERVICES</h2>
  <p class="section-sub" style="top:96px">Maybe you don't want to purchase one of our pre-made SEO packages. No problem.</p>
  <div class="feature on" style="left:232px;top:171px">
    <div class="ring"><svg width="56" height="56" viewBox="0 0 56 56" fill="none" stroke="#fff" stroke-width="5" stroke-linecap="round"><path d="M12 44 L44 12"/><path d="M12 12 L44 44"/><circle cx="12" cy="12" r="6"/><circle cx="44" cy="44" r="6"/></svg></div>
    <div class="label">BRANDING</div>
  </div>
  <div class="feature" style="left:487px;top:171px">
    <div class="ring"><svg width="56" height="50" viewBox="0 0 56 50" fill="none" stroke="#999" stroke-width="3"><rect x="4" y="4" width="48" height="32" rx="2"/><path d="M20 46h16M28 36v10"/><path d="M20 28 L38 12" stroke-linecap="round"/></svg></div>
    <div class="label">DESIGN</div>
  </div>
  <div class="feature" style="left:741px;top:171px">
    <div class="ring"><svg width="60" height="44" viewBox="0 0 60 44" fill="none" stroke="#999" stroke-width="3"><rect x="10" y="4" width="40" height="28" rx="2"/><path d="M2 38h56"/><circle cx="30" cy="18" r="5"/></svg></div>
    <div class="label">DEVELOPMENT</div>
  </div>
</section>

<section class="contact">
  <h2>Get In Touch</h2>
  <p class="lead">The lorem ipsum text is typically a mangled section</p>
  <div class="field" style="left:255px;top:185px;width:334px;height:56px">Your name</div>
  <div class="field" style="left:616px;top:185px;width:328px;height:56px">Your Email</div>
  <div class="field textarea" style="left:255px;top:262px;width:689px;height:211px">Your Message</div>
</section>

<footer class="site-footer">
  <div class="brand"><span class="brand-dot"></span><span class="brand-name">RankOrchard</span></div>
  <p>Lorem ipsum dolor sit amet, consectetur adipisicing elit, sed do eiusmod tempor incididunt ut labore</p>
  <div class="social" aria-label="Social links"><span></span><span></span><span></span><span></span></div>
</footer>

</body>
</html>
```